Business Card Design Project - Photographer

Photography business needs a logo. I would like to see creative licence on options on 1 & 2 sided. I really like the concept of a fully / partially frosted design. I have already used ArtHive for my Logo, so I am looking for the same level of assistance with this project.

If you have any questions please let me know

Cheers Dorian

Reason: Unsure why but the duration was not even a day long

Industry/Entity Type

Business

Requirements
Must have
• These are my contact details
Name: Dorian Welcombe
Mobile: 0438 612 907
email: dorian@brightlensstudio.com.au
Website: www.brightlensstudio.com.au
Nice to have
• Facebook: https://www.facebook.com/BrightLensStudioOz

```html
<!DOCTYPE html>
<html lang="en">
<head>
<meta charset="utf-8">
<title>Bright Lens Studio – Business Card</title>
<link href="https://fonts.googleapis.com/css2?family=Questrial&family=Share+Tech+Mono&display=swap" rel="stylesheet">
<style>
  :root {
    --backdrop: #1c1c1e;
    --frost-light: #d9dadc;
    --frost-mid: #bfc0c3;
    --frost-edge: #a9aaad;
    --band: #111112;
    --accent-red: #d8231f;
    --ink-dark: #3a3a3c;
    --bracket: #4a4a4d;
  }
  html, body {
    margin: 0;
    width: 1200px;
    height: 900px;
    overflow: hidden;
    background: var(--backdrop);
  }
  .card {
    position: absolute;
    left: 100px;
    top: 164px;
    width: 1000px;
    height: 572px;
    border-radius: 28px;
    overflow: hidden;
    background: linear-gradient(160deg, var(--frost-light) 0%, var(--frost-mid) 60%, var(--frost-edge) 100%);
    box-shadow: inset 0 0 0 2px rgba(255,255,255,0.35);
  }
  .card-frame {
    position: absolute;
    inset: 0;
  }
  .brand {
    position: absolute;
    left: 230px;
    width: 540px;
    top: 190px;
    text-align: center;
  }
  .brand-name {
    font-family: "Questrial", sans-serif;
    font-weight: 400;
    font-size: 38px;
    letter-spacing: 2px;
    color: var(--accent-red);
    margin: 0;
    line-height: 1;
    white-space: nowrap;
  }
  .brand-tagline {
    font-family: "Questrial", sans-serif;
    font-size: 22px;
    letter-spacing: 2px;
    color: var(--ink-dark);
    margin: 14px 0 0;
  }
  .contact-band {
    position: absolute;
    left: 0;
    right: 0;
    bottom: 0;
    height: 146px;
    background: var(--band);
    padding: 22px 44px 0;
    box-sizing: border-box;
    font-family: "Share Tech Mono", monospace;
    color: var(--accent-red);
    font-size: 30px;
    letter-spacing: 1px;
    text-transform: uppercase;
  }
  .contact-row {
    display: flex;
    align-items: center;
    gap: 34px;
    height: 50px;
    white-space: nowrap;
  }
  .contact-item {
    display: flex;
    align-items: center;
    gap: 12px;
  }
  .contact-icon {
    width: 22px;
    height: 30px;
    fill: var(--accent-red);
  }
  .iso-badge {
    display: flex;
    flex-direction: column;
    align-items: center;
    font-size: 14px;
    line-height: 1;
    gap: 3px;
  }
  .iso-badge .box {
    width: 16px;
    height: 14px;
    background: var(--accent-red);
  }
</style>
</head>
<body>
  <section class="card" aria-label="Bright Lens Studio business card">
    <svg class="card-frame" viewBox="0 0 1000 572" aria-hidden="true">
      <g fill="none" stroke="var(--bracket)" stroke-width="6" stroke-linecap="round" stroke-linejoin="round">
        <path class="viewfinder-outer" d="M120 160 H90 V300 H120"/>
        <path class="viewfinder-outer" d="M880 160 H910 V300 H880"/>
        <path class="viewfinder-inner" d="M260 80 H215 V400 H260"/>
        <path class="viewfinder-inner" d="M740 80 H785 V400 H740"/>
      </g>
    </svg>

    <div class="brand">
      <h1 class="brand-name">BRIGHT LENS STUDIO</h1>
      <p class="brand-tagline">light, framed true</p>
    </div>

    <footer class="contact-band">
      <div class="contact-row">
        <span class="contact-item">
          <svg class="contact-icon" viewBox="0 0 22 30" aria-label="Phone"><path d="M13 0 L2 17 H10 L7 30 L20 11 H12 Z"/></svg>
          0438 612 907
        </span>
        <span class="contact-item">dorian@brightlensstudio.com.au</span>
      </div>
      <div class="contact-row">
        <span class="contact-item">www.brightlensstudio.com.au</span>
        <span class="iso-badge"><span class="box"></span>ISO</span>
        <span class="contact-item">Dorian Welcombe</span>
      </div>
    </footer>
  </section>
</body>
</html>
```